Flyer-Design für Touroperator/Eventveranstalter
Zielgruppe
Die Zielgruppe sind ausschliesslich Frauen zwischen 25 und 55 Jahren.
Meine Firma organisiert unvergessliche Städtetrips mit Programm vor Ort.
Städte in Osteuropa wobei derzeit nur im Programm Warschau und Prag.
Mit dem Flyer soll die Sommertour Warschau beworben werden.
Die Städtetrips sind höherer Standard und exklusiv.
Aufgabenstellung
Der Flyer soll nicht zu groß sein z.B. DIN A6 sein und Vorder- und Rückseite haben.
Jedenfalls soll der Flyer handlich bleiben, so dass er sich z.B. als Beilage in Einkaufstüten eignet etc.
Dafür muss der beigefügte Text gekürzt werden. Mein Entwurf hat zu viel Text aber ich weiss nicht, wieviel auf einen Flyer passt. Außerdem muss der Flyer unbedingt mein Logo und meine Firmenangaben beinhalten.
Der Flyer soll das beigefügte Frauengruppenfoto beinhalten und ein Foto aus den beigefügten Warschau Fotos.
Vielleicht kann man auch mehrere Fotos zusammen schneiden.

```html
<!DOCTYPE html>
<html lang="de">
<head>
<meta charset="utf-8">
<title>Sommertour Warschau – Flyer</title>
<link href="https://fonts.googleapis.com/css2?family=Lobster&family=Luckiest+Guy&family=Open+Sans:wght@600;700&family=Arimo:wght@700&display=swap" rel="stylesheet">
<style>
:root{
  --brown:#a87a44;
  --brown-dark:#8d6434;
  --pink:#cc2366;
  --pink-soft:#e8a3c0;
  --white:#ffffff;
  --navy:#3d3a8a;
  --sky-top:#2c4f86;
  --sky-mid:#5d79a8;
  --city-warm:#c98a5a;
  --city-dark:#3a2f3e;
  --paper:#ffffff;
}
*{margin:0;padding:0;box-sizing:border-box}
html,body{width:836px;height:1200px;overflow:hidden;background:var(--paper)}
.canvas{position:relative;width:836px;height:1200px;background:var(--paper)}
.display{font-family:"Luckiest Guy","Impact","Arial Black",sans-serif;font-weight:400}

/* front side */
.front{position:absolute;left:5px;top:5px;width:827px;height:586px;overflow:hidden}
.front-photo{position:absolute;inset:0;
  background:linear-gradient(180deg,var(--sky-top) 0%,var(--sky-mid) 25%,#8a7f95 42%,var(--city-warm) 60%,var(--city-dark) 100%)}
.brand{position:absolute;font-family:"Open Sans",sans-serif;font-weight:700;color:var(--brown);
  display:flex;align-items:center;gap:10px;white-space:nowrap}
.brand .dot{width:14px;height:14px;border-radius:50%;background:var(--brown);flex:none}
.front .brand{left:596px;top:108px;font-size:30px;color:var(--white)}
.front .brand .dot{background:var(--white)}
.title-band{position:absolute;left:0;top:228px;width:100%;height:90px;background:rgba(255,255,255,.72);
  display:flex;align-items:center;justify-content:center}
.title-band h1{font-family:"Lobster",cursive;font-weight:400;font-size:62px;line-height:1;color:var(--navy);
  letter-spacing:1px;white-space:nowrap}
.slogan{position:absolute;left:140px;top:382px;width:560px;height:50px;background:rgba(239,160,195,.75);
  transform:rotate(-4deg);display:flex;align-items:center;justify-content:center;
  border-top:2px solid var(--pink);white-space:nowrap;
  font-family:"Open Sans",sans-serif;font-weight:700;font-size:23px;letter-spacing:3px;color:var(--pink)}
.cta{position:absolute;right:30px;top:450px;font-size:52px;line-height:1;color:var(--white);white-space:nowrap;
  -webkit-text-stroke:3px var(--brown);paint-order:stroke fill;letter-spacing:1px}
.front-bar{position:absolute;left:0;bottom:0;width:100%;height:54px;background:var(--brown);
  display:flex;align-items:center;justify-content:space-between;padding:0 30px;white-space:nowrap;
  font-family:"Open Sans",sans-serif;font-weight:700;font-size:18px;color:var(--white)}

/* back side */
.back{position:absolute;left:5px;top:604px;width:827px;height:592px;overflow:hidden;border:1px solid #ddd}
.back-photo{position:absolute;inset:0;
  background:radial-gradient(ellipse at 30% 40%,#f3e7e3 0%,#eef1f6 55%,#e4ecf5 100%)}
.back-title{position:absolute;left:58px;top:28px;width:720px;color:var(--brown);white-space:nowrap;line-height:1}
.back-title .small{font-size:34px}
.back-title .big{font-size:48px}
.tours{position:absolute;left:40px;top:284px;transform:rotate(-90deg);transform-origin:0 0;white-space:nowrap;
  font-family:"Open Sans",sans-serif;font-weight:700;font-size:20px;color:var(--pink);line-height:28px}
.star{position:absolute;left:245px;top:92px;width:210px;height:195px}
.star-text{position:absolute;left:245px;top:132px;width:210px;text-align:center;
  font-family:"Lobster",cursive;font-size:29px;line-height:31px;color:var(--pink);
  -webkit-text-stroke:4px var(--white);paint-order:stroke fill}
.list{font-family:"Open Sans",sans-serif;font-weight:700;color:var(--pink);list-style:none;white-space:nowrap}
.list-top{position:absolute;left:482px;top:100px;font-size:20px;line-height:29px}
.highlights{position:absolute;left:482px;top:226px;font-size:42px;line-height:1;white-space:nowrap;
  color:var(--brown);-webkit-text-stroke:3px var(--white);paint-order:stroke fill}
.list-bottom{position:absolute;left:54px;top:300px;font-size:20px;line-height:28px}
.back .brand{left:620px;top:340px;font-size:26px}
.company{position:absolute;left:0;top:470px;width:100%;text-align:center;background:rgba(255,255,255,.8);white-space:nowrap;
  font-family:"Arimo",sans-serif;font-weight:700;font-size:27px;color:var(--brown);padding:4px 0}
.back-bar{position:absolute;left:0;bottom:0;width:100%;height:84px;background:var(--brown);white-space:nowrap;
  text-align:center;font-family:"Arimo",sans-serif;font-weight:700;color:var(--white);padding-top:4px}
.back-bar .addr{font-size:22px;line-height:25px}
.back-bar .contact{font-size:16px;line-height:20px}
.back-bar .web{font-size:28px;line-height:32px}
</style>
</head>
<body>
<div class="canvas">

  <section class="front">
    <div class="front-photo" role="img" aria-label="Skyline von Warschau in der Abenddämmerung mit Hochhäusern und beleuchteten Straßen"></div>
    <div class="brand"><span class="dot"></span>Belle Voyage</div>
    <div class="title-band"><h1>Kurztrip nach WARSCHAU</h1></div>
    <div class="slogan">WIR PLANEN UND IHR HABT SPASS!</div>
    <div class="cta display">JETZT BUCHEN</div>
    <div class="front-bar">
      <span>info@bellevoyage.de</span>
      <span>0171-5550123</span>
      <span>WWW.BELLEVOYAGE.DE</span>
    </div>
  </section>

  <section class="back">
    <div class="back-photo" role="img" aria-label="Gruppe fröhlicher Frauen, die feiern, in hellen, verblassten Farben"></div>
    <h2 class="back-title display"><span class="small">UNSERE SOMMERTOUR </span><span class="big">WARSCHAU</span></h2>

    <ul class="list tours">
      <li>Retro-Bus Tour</li>
      <li>Altstadtbummel</li>
      <li>Shopping Tour</li>
      <li>Natur pur - Parks</li>
      <li>Bootsfahrt</li>
    </ul>

    <svg class="star" viewBox="0 0 220 200" aria-hidden="true">
      <polygon fill="#a87a44" points="110,0 128,52 180,22 160,74 220,84 168,112 200,160 146,146 138,200 110,158 82,200 74,146 20,160 52,112 0,84 60,74 40,22 92,52"/>
    </svg>
    <div class="star-text">sich ganz<br>wie ein STAR<br>fühlen</div>

    <ul class="list list-top">
      <li>Barbecue am Strand</li>
      <li>Nightlife mit Bar-Hopping</li>
      <li>Essen in Top-Restaurants</li>
      <li>Betreuung vor Ort</li>
    </ul>
    <div class="highlights display">HIGHLIGHTS</div>

    <ul class="list list-bottom">
      <li>Programm wird nach Euren Interessen angepasst</li>
      <li>Schlecht Wetter Programm inklusive</li>
      <li>(Wellness, Kosmetik)</li>
      <li>Chauffeur bringt Euch zu Eurem Hotel</li>
      <li>Im Zimmer erwartet Euch eine Überraschung</li>
    </ul>

    <div class="brand"><span class="dot"></span>Belle Voyage</div>

    <div class="company">Clara &amp; Co. Reisen und Events GmbH</div>
    <div class="back-bar">
      <div class="addr">Lindenweg 14, 50667 Köln</div>
      <div class="contact">0171 - 5550123, info@bellevoyage.de</div>
      <div class="web">www.bellevoyage.de</div>
    </div>
  </section>

</div>
</body>
</html>
```